Packaging label for launch of sun dried tomato products.

Established family farm in South Africa growing fruit for the production of dried fruit. We need a packaging label for the launch of our sun dried tomato products ie dried tomatoes in olive oil, dried tomato flakes and tomato powder. Packaging will be a round glass "jam jar" and spice shaker bottle. Due to limited amount of product available we cannot market to the masses, but rather focus on conveying a message of quality and exclusivity.

Target Market(s)

Home chef

Industry/Entity Type

Food

Font styles to use
Serif

Requirements
Nice to have
• Include the farm name in the design. KEVANTO

```html
<!DOCTYPE html>
<html lang="en">
<head>
<meta charset="utf-8">
<title>KEVANTO Sun-Dried Tomatoes – Front Label</title>
<link rel="stylesheet" href="https://fonts.googleapis.com/css2?family=Oswald:wght@300;400;700&family=Pinyon+Script&family=Roboto+Slab:wght@400;700&display=swap">
<style>
  :root {
    --page-bg: #f5f5f5;
    --tomato-red: #cc2414;
    --deep-red: #b01c12;
    --salmon: #ea7050;
    --salmon-light: #f6c4b0;
    --herb-green: #1e9a3a;
    --ink: #1c1c1c;
    --white: #ffffff;
  }
  * { margin: 0; padding: 0; box-sizing: border-box; }
  html, body {
    width: 771px; height: 1200px; overflow: hidden;
    background: var(--page-bg);
  }
  .canvas {
    position: relative; width: 771px; height: 1200px;
    display: flex; align-items: center; justify-content: center;
  }
  .front-label { width: 705px; height: 490px; display: block; }
  .brand-name { font-family: "Roboto Slab", serif; font-weight: 700; fill: var(--tomato-red); letter-spacing: 4px; }
  .headline-sun { font-family: "Oswald", sans-serif; font-weight: 700; fill: var(--herb-green); }
  .headline-tomatoes { font-family: "Oswald", sans-serif; font-weight: 700; fill: var(--tomato-red); }
  .headline-oil { font-family: "Oswald", sans-serif; font-weight: 700; fill: var(--deep-red); }
  .flavour-script { font-family: "Pinyon Script", cursive; fill: var(--ink); }
  .tagline { font-family: "Roboto Slab", serif; font-weight: 400; fill: var(--ink); }
  .net-weight { font-family: "Oswald", sans-serif; font-weight: 300; fill: var(--white); }
</style>
</head>
<body>
<main class="canvas">
  <svg class="front-label" viewBox="0 0 1116 775" xmlns="http://www.w3.org/2000/svg">
    <!-- base band -->
    <rect class="band-salmon" x="0" y="0" width="1116" height="775" fill="var(--salmon)"/>

    <!-- left patterned band -->
    <g role="img" aria-label="Tomato, tomato slice and herb sprig line pattern on red">
      <polygon points="0,0 280,0 280,372 0,465" fill="var(--tomato-red)"/>
    </g>
    <!-- right patterned bands -->
    <g role="img" aria-label="Tomato and herb line pattern on red">
      <polygon points="840,0 1116,0 1116,85 840,177" fill="var(--tomato-red)"/>
      <polygon points="840,587 1116,497 1116,775 310,775" fill="var(--tomato-red)"/>
    </g>

    <!-- white label panel -->
    <path class="label-panel" d="M257 0 H862 V678 a20 20 0 0 1 -20 20 H277 a20 20 0 0 1 -20 -20 Z" fill="var(--white)"/>

    <!-- top rules -->
    <g class="top-rules" stroke="var(--tomato-red)">
      <line x1="290" y1="38" x2="430" y2="38" stroke-width="3"/>
      <line x1="290" y1="45" x2="430" y2="45" stroke-width="1.5"/>
      <line x1="690" y1="38" x2="826" y2="38" stroke-width="3"/>
      <line x1="690" y1="45" x2="826" y2="45" stroke-width="1.5"/>
    </g>

    <text class="brand-name" x="558" y="112" text-anchor="middle" font-size="52">KEVANTO</text>

    <text class="headline-sun" x="570" y="268" text-anchor="middle" font-size="112" textLength="385" lengthAdjust="spacingAndGlyphs">SUN-DRIED</text>
    <text class="headline-tomatoes" x="558" y="410" text-anchor="middle" font-size="170" textLength="515" lengthAdjust="spacingAndGlyphs">TOMATOES</text>
    <text class="headline-oil" x="560" y="490" text-anchor="middle" font-size="78" textLength="300" lengthAdjust="spacingAndGlyphs">IN OLIVE OIL</text>

    <!-- tomato sketch area -->
    <ellipse class="tomato-sketch" cx="515" cy="628" rx="92" ry="68" fill="var(--salmon-light)" opacity="0.55" role="img" aria-label="Line sketch of halved tomatoes"/>

    <text class="flavour-script" x="548" y="598" text-anchor="middle" font-size="82" textLength="315" lengthAdjust="spacingAndGlyphs" transform="rotate(-12 548 590)">With herbs</text>

    <!-- certificate badge -->
    <circle class="badge" cx="775" cy="598" r="46" fill="none" stroke="var(--ink)" stroke-width="2" role="img" aria-label="Gluten free badge"/>

    <line class="bottom-rule" x1="290" y1="645" x2="826" y2="645" stroke="var(--tomato-red)" stroke-width="3"/>
    <text class="tagline" x="558" y="680" text-anchor="middle" font-size="24" textLength="520" lengthAdjust="spacing">SUSTAINABLE FARMING PRODUCT</text>

    <text class="net-weight" x="558" y="740" text-anchor="middle" font-size="32" textLength="345" lengthAdjust="spacingAndGlyphs">NET WT. 7 FL. OZ. (205 ML)</text>
  </svg>
</main>
</body>
</html>
```